Build Your Own Shake Menu Design

- will be printed on countertop acrylic menu stands that are a foot by a foot

Files:
- document attached for the menu contents
*file name: SHAKEMENU
- sample menu images (these are giant acrylic menu boards that are in my shop)
*file name: newest shave ice menu, newest spi rolls menu (JPG)
-picture of the shop where the menus will be placed
*file name: shop (PNG)

```html
<!DOCTYPE html>
<html lang="en">
<head>
<meta charset="utf-8">
<title>Build Your Own Shake Menu</title>
<link href="https://fonts.googleapis.com/css2?family=Lobster&family=Space+Grotesk:wght@400;500;600;700&display=swap" rel="stylesheet">
<style>
:root{
  --navy:#012a6e;
  --gold:#fcc200;
  --cream:#f5ead6;
  --ink:#151515;
  --white:#ffffff;
  --bg-top:#8e2a2c;
  --bg-bottom:#2b2b2e;
}
*{margin:0;padding:0;box-sizing:border-box}
html,body{width:1200px;height:1009px;overflow:hidden}
body{
  position:relative;
  background:linear-gradient(180deg,var(--bg-top) 0%,#6a2427 30%,#3a2a2c 65%,var(--bg-bottom) 100%);
  font-family:"Space Grotesk",sans-serif;
  color:var(--white);
}
.photo{position:absolute}
.photo-splash{left:0;top:0;width:170px;height:190px;border-radius:40% 60% 55% 45%;background:radial-gradient(circle at 45% 50%,#e4412e,#a81e1a 60%,rgba(168,30,26,0) 75%)}
.photo-plate{right:0;top:0;width:150px;height:140px;border-radius:0 0 0 70px;background:radial-gradient(circle at 60% 40%,#e0b27a,#c58245 45%,#2c2c2c 75%)}
.photo-pasta{left:0;bottom:0;width:130px;height:110px;border-radius:0 70px 0 0;background:radial-gradient(circle at 40% 60%,#d9552f,#b5391f 50%,#f2f2f2 70%)}
.photo-cone-choc{right:10px;top:670px;width:70px;height:145px;border-radius:35px 35px 6px 6px;background:linear-gradient(180deg,#6b3a26 0 38%,#d9a25c 38% 100%)}
.photo-cone-pink{right:10px;top:820px;width:70px;height:145px;border-radius:35px 35px 6px 6px;background:linear-gradient(180deg,#f08aa6 0 38%,#d9a25c 38% 100%)}

.menu{position:absolute;left:82px;top:73px;width:1036px;height:864px;background:var(--cream)}

.card{position:absolute;background:var(--navy)}
.card-head{position:absolute;left:0;top:0;width:100%;background:var(--gold);color:var(--navy);font-family:"Lobster",cursive;font-weight:400;display:flex;align-items:center;justify-content:center;text-align:center}

.toppings{left:14px;top:19px;width:323px;height:590px}
.toppings .card-head{height:69px;font-size:18px;line-height:25px}
.topping-list{position:absolute;left:17px;right:12px;top:85px;list-style:none;font-size:14px;font-weight:500;line-height:26.4px}
.topping-list li{display:flex;justify-content:space-between}
.topping-list li span:first-child{white-space:nowrap}
.topping-list .price{flex:none;margin-left:8px}

.icecream{left:355px;top:19px;width:323px;height:254px}
.icecream .card-head,.drinks .card-head{height:69px;font-size:25px}
.price-list{position:absolute;left:20px;right:16px;top:83px;list-style:none;font-size:14px;font-weight:500;line-height:26.4px}
.price-list li{display:flex;justify-content:space-between}
.scoops{position:absolute;left:62px;top:218px;width:196px;height:52px;display:flex;justify-content:space-between}
.scoop{width:52px;height:52px;border-radius:50%}
.scoop-pink{background:radial-gradient(circle at 40% 35%,#ff9ec0,#e8507f)}
.scoop-berry{background:radial-gradient(circle at 40% 35%,#e0506a,#a0193a)}
.scoop-choc{background:radial-gradient(circle at 40% 35%,#a57155,#6a3f2b)}

.drinks{left:694px;top:22px;width:323px;height:253px}
.drinks .price-list{top:86px;left:18px}

.build-head{position:absolute;left:355px;top:315px;width:473px;height:69px;background:var(--gold);color:var(--navy);font-family:"Lobster",cursive;font-weight:400;font-size:17px;line-height:27px;padding:9px 0 0 21px}
.build-price{position:absolute;left:828px;top:315px;width:189px;height:69px;background:var(--ink);color:var(--gold);font-weight:700;font-size:27px;display:flex;align-items:center;justify-content:center}
.build-body{position:absolute;left:355px;top:384px;width:662px;height:225px;background:var(--navy);display:grid;grid-template-columns:1fr 1fr;padding:22px 20px 0 32px;column-gap:20px;row-gap:15px;align-content:start}
.offer h3{font-size:14px;font-weight:700;line-height:18px;margin-bottom:3px}
.offer p{font-size:14px;line-height:26.4px}

.food-strip{position:absolute;left:132px;top:617px;width:776px;height:56px;border-radius:28px;background:linear-gradient(90deg,#e7c79a,#cfa06b,#e8d3b2,#b98a5a,#e7c79a)}

.spoons{position:absolute;left:0;top:682px;width:522px;height:182px;background:var(--gold);color:var(--navy)}
.spoons p{position:absolute;left:12px;top:16px;width:466px;font-size:14px;line-height:26.4px}
.spoons-price{position:absolute;left:0;top:133px}
.spoons-price span{position:absolute;left:0;top:0;width:344px;height:49px;display:flex;align-items:center;justify-content:center;color:var(--gold);font-weight:700;font-size:19px}

.daily{position:absolute;left:522px;top:682px;width:514px;height:182px;background:var(--navy)}
.daily-tab{position:absolute;right:0;top:0}
.daily-tab span{position:absolute;right:0;top:0;width:300px;height:49px;display:flex;align-items:center;justify-content:center;color:var(--navy);font-family:"Lobster",cursive;font-weight:400;font-size:20px;padding-left:30px}
.daily-body{position:absolute;left:14px;top:70px;right:20px;display:grid;grid-template-columns:1fr 1fr;column-gap:20px}
.daily-body .offer p{line-height:21.6px}
</style>
</head>
<body>
<div class="photo photo-splash" role="img" aria-label="Splash of red fruit drink with orange slice"></div>
<div class="photo photo-plate" role="img" aria-label="Plate of grilled chicken with vegetables"></div>
<div class="photo photo-pasta" role="img" aria-label="Plate of penne pasta"></div>
<div class="photo photo-cone-choc" role="img" aria-label="Chocolate ice cream cone"></div>
<div class="photo photo-cone-pink" role="img" aria-label="Strawberry ice cream cone"></div>

<main class="menu">
  <section class="card toppings">
    <h2 class="card-head">Choose Up To 2 Items For<br>Your Shake</h2>
    <ul class="topping-list">
      <li><span>Cookie Dough-Peanut Butter<br>Cup-Crunchbar-</span><span class="price">$5.75</span></li>
      <li><span>Mint Melts-Toffee- -Chip Cookies-<br>Graham Crackers-</span><span class="price">$5.99</span></li>
      <li><span>Cocoa Cookie -Chocolate Chips-<br>White Chocolate Chips-</span><span class="price">$5.75</span></li>
      <li><span>Rainbow Sprinkles-Cupcake<br>Bites-Candy Gems</span><span class="price">$5.99</span></li>
      <li><span>Nuts-Almonds-Strawberries-<br>Banana-Cherries</span><span class="price">$5.75</span></li>
      <li><span>Sailor Crunch-Cinnamon Sugar<br>Crisp</span><span class="price">$5.99</span></li>
      <li><span>Fruity Pops- Chocolate Pops</span><span class="price">$5.75</span></li>
      <li><span>Peanut Butter Drizzle -Chocolate<br>Drizzle-</span><span class="price">$6.25</span></li>
      <li><span>Strawberry Drizzle-Raspberry<br>Drizzle -</span><span class="price">$6.49</span></li>
      <li><span>Marshmallow Drizzle</span><span class="price">$6.25</span></li>
    </ul>
  </section>

  <section class="card icecream">
    <h2 class="card-head">Ice Cream</h2>
    <ul class="price-list">
      <li><span>15 ounce Regular</span><span>$5.75</span></li>
      <li><span>15 ounce Specialty Base</span><span>$6.25</span></li>
      <li><span>18 ounce Large</span><span>$5.99</span></li>
      <li><span>18 ounce Specialty Base</span><span>$6.49</span></li>
    </ul>
    <div class="scoops" role="img" aria-label="Three ice cream scoops: strawberry, berry and chocolate">
      <span class="scoop scoop-pink"></span><span class="scoop scoop-berry"></span><span class="scoop scoop-choc"></span>
    </div>
  </section>

  <section class="card drinks">
    <h2 class="card-head">Drinks</h2>
    <ul class="price-list">
      <li><span>Water</span><span>$1.00</span></li>
      <li><span>Cola</span><span>$1.99</span></li>
      <li><span>Lemon-Lime</span><span>$1.99</span></li>
      <li><span>Tea</span><span>$1.99</span></li>
      <li><span>Sport Drink Fruit Punch</span><span>$1.99</span></li>
    </ul>
  </section>

  <h2 class="build-head">Create Your Own Shake Menu Choose Your Base<br>Standard Base- Van - Chocolate</h2>
  <div class="build-price">$120.00</div>
  <section class="build-body">
    <div class="offer"><h3>Lorem ipsum dolor sit amet</h3><p>Lorem ipsum dolor sit amet, consectetur adipiscing elit, sed do eiusmod</p></div>
    <div class="offer"><h3>Lorem ipsum dolor sit amet</h3><p>Lorem ipsum dolor sit amet, consectetur adipiscing elit, sed do eiusmod</p></div>
    <div class="offer"><h3>Lorem ipsum dolor sit amet</h3><p>Lorem ipsum dolor sit amet, consectetur adipiscing elit, sed do eiusmod</p></div>
    <div class="offer"><h3>Lorem ipsum dolor sit amet</h3><p>Lorem ipsum dolor sit amet, consectetur adipiscing elit, sed do eiusmod</p></div>
  </section>

  <div class="food-strip" role="img" aria-label="Row of plated pastries and snacks"></div>

  <section class="spoons">
    <p>Its for our Color Changing Spoons Color Changing Spoons are .50 cents and come in 3 colorsWhite to Blue -Pink to Purple- White to Confetti Im hoping for some kind of image for them so kids can tell &nbsp;what they areSame thing for the drinks, the visuals help.</p>
    <div class="spoons-price">
      <svg width="344" height="49" viewBox="0 0 344 49"><polygon points="0,0 305,0 344,49 0,49" fill="var(--navy)"/></svg>
      <span>$25.00</span>
    </div>
  </section>

  <section class="daily">
    <div class="daily-tab">
      <svg width="328" height="49" viewBox="0 0 328 49" style="display:block;margin-left:auto"><polygon points="0,0 328,0 328,49 26,49" fill="var(--gold)"/></svg>
      <span>Daily Offers</span>
    </div>
    <div class="daily-body">
      <div class="offer"><h3>Lorem ipsum dolor sit amet</h3><p>Lorem ipsum dolor sit amet, consectetur adipiscing elit, sed do eiusmod</p></div>
      <div class="offer"><h3>Lorem ipsum dolor sit amet</h3><p>Lorem ipsum dolor sit amet, consectetur adipiscing elit, sed do eiusmod</p></div>
    </div>
  </section>
</main>
</body>
</html>
```